24Std Betreuung Flyer Senioren
Zielgruppe
Wir vermitteln Ihnen Pflegekräfte aus Polen in 24h Betreuung. Zu diesem Zweck arbeiten wir mit unseren Partnerunternehmen in Polen und Litauen, welche ihre Pflegekraft im Rahmen der EU Dienstleistungsfreiheit legal nach Deutschland vermitteln. Das von uns vermittelte Personal ist freundlich und gut ausgebildet und verfügt über ausreichende bis gute Deutschkenntnisse. Unsere Agentur übernimmt die Koordinierung und Klärung aller Angelegenheiten für die An- und Abreise ihrer Pflegekraft. Das Personal wohnt mit der pflegebürftigen Person zusammen, wodurch wir eine 24h Betreuung realisieren können.
Aufgabenstellung
Seniorengerecht und nicht zu modern, übersichtlich nicht zu klein geschrieben evtl mit lizenzfreien Bildern von Senioren
Format: 6 seitig Wickelfalz
Informationen auf ww.altershilfe-plus.de

```html
<!DOCTYPE html>
<html lang="de">
<head>
<meta charset="utf-8">
<title>Altershilfe Plus – 24h Betreuung Flyer</title>
<link href="https://fonts.googleapis.com/css2?family=Arimo:wght@400;700&display=swap" rel="stylesheet">
<style>
  :root {
    --bg: #e8e8e9;
    --paper: #fbfcfd;
    --blue: #2a86bf;
    --blue-dark: #1f6fa6;
    --blue-mid: #3d9bd0;
    --blue-light: #7fbfe3;
    --blue-pale: #a9d3ee;
    --text-blue: #2c7fb8;
    --white: #ffffff;
  }
  * { margin: 0; padding: 0; box-sizing: border-box; }
  html, body { width: 1200px; height: 960px; overflow: hidden; }
  body {
    background: var(--bg);
    font-family: "Arimo", Arial, sans-serif;
    display: flex; align-items: center; justify-content: center;
  }
  .flyer {
    display: flex;
    width: 1074px; height: 760px;
    background: var(--paper);
    box-shadow: 0 18px 40px rgba(0,0,0,.18);
  }
  .panel {
    position: relative;
    width: 358px; height: 100%;
    overflow: hidden;
    display: flex; flex-direction: column;
    background: var(--paper);
  }
  .panel + .panel { border-left: 1px solid #e2e6ea; }

  /* shared bottom stripes */
  .stripes { position: absolute; left: 0; right: 0; bottom: 0; height: 62px; }
  .stripes span { position: absolute; left: 0; right: 0; display: block; }
  .stripes .s1 { top: 0; height: 10px; background: var(--blue-pale); }
  .stripes .s2 { top: 18px; height: 12px; background: var(--blue-light); }
  .stripes .s3 { top: 38px; height: 24px; background: var(--blue-mid); }

  .rule { height: 8px; background: var(--blue-mid); margin-top: 6px; }

  /* panel 1 */
  .intro {
    height: 405px;
    background: linear-gradient(160deg, #5fb1de 0%, var(--blue) 55%, var(--blue-dark) 100%);
    color: var(--white);
    font-size: 15.2px; line-height: 1.62;
    padding: 26px 22px 0 28px;
    text-align: justify;
    text-align-last: left;
  }
  .photo { flex: none; }
  .photo--group {
    height: 245px;
    background: linear-gradient(135deg, #f2efec 0%, #d9c7b4 40%, #eef1f5 70%, #c7b39c 100%);
  }

  /* panel 2 */
  .photo--garden {
    height: 360px;
    background: linear-gradient(160deg, #7aa070 0%, #b9ccaa 35%, #d69a8e 65%, #e9ddd2 100%);
  }
  .body-text {
    color: var(--text-blue);
    font-size: 15.5px; line-height: 1.6;
    padding: 26px 30px 0;
    text-align: center;
  }
  .body-text p + p { margin-top: 24px; }

  /* panel 3 cover */
  .cover-logo {
    height: 215px;
    display: flex; align-items: center; justify-content: center; gap: 12px;
    background: var(--white);
  }
  .brand-dot { width: 26px; height: 26px; border-radius: 50%; background: var(--blue); }
  .brand-name { font-size: 30px; font-weight: 400; color: var(--blue-dark); }
  .headline {
    height: 110px;
    background: linear-gradient(180deg, #f1f4f6, #eef2ef);
    color: var(--text-blue);
    text-align: center;
    padding-top: 24px;
  }
  .headline .kicker { font-size: 20px; }
  .headline .main { font-size: 30px; font-weight: 700; margin-top: 2px; }
  .photo--hands {
    flex: 1;
    background: linear-gradient(160deg, #eef0e6 0%, #cfdcb8 40%, #e8d2c3 60%, #b7d09f 100%);
  }
</style>
</head>
<body>
<main class="flyer">
  <section class="panel panel--intro">
    <div class="intro">
      Wir vermitteln Ihnen Pflegekräfte aus Polen in 24h Betreuung. Zu diesem Zweck arbeiten wir mit unseren Partnerunternehmen in Polen, welche ihre Pflegekraft im Rahmen der EU Dienstleistungsfreiheit legal nach Deutschland vermitteln. Das von uns vermittelte Personal ist freundlich und gut ausgebildet und verfügt über ausreichende bis gute Deutschkenntnisse. Unsere Agentur übernimmt die Koordinierung und Klärung aller Angelegenheiten für die An- und Abreise ihrer Pflegekraft. Das Personal wohnt mit der pflegebürftigen Person zusammen, wodurch wir eine 24h Betreuung realisieren können.
    </div>
    <div class="rule"></div>
    <div class="photo photo--group" role="img" aria-label="Foto: Gruppe fröhlicher Senioren auf einem Sofa mit einem Laptop"></div>
    <div class="stripes"><span class="s1"></span><span class="s2"></span><span class="s3"></span></div>
  </section>

  <section class="panel panel--consult">
    <div class="photo photo--garden" role="img" aria-label="Foto: Seniorin mit Tasse im Garten unter Bäumen"></div>
    <div class="rule"></div>
    <div class="body-text">
      <p>In einer eingehenden Beratung bei Ihnen zu Hause erstellen wir eine Anamnese und unterstützen bei der Auswahl des geeigneten Personals, um die beste Entscheidung für Sie zu treffen.</p>
      <p>Gerne beraten wir Sie in einer Bedarfsanalyse, um so gemeinsam mit Ihnen die richtige Pflegekraft zu finden.</p>
    </div>
    <div class="stripes"><span class="s1"></span><span class="s2"></span><span class="s3"></span></div>
  </section>

  <section class="panel panel--cover">
    <div class="cover-logo">
      <span class="brand-dot"></span>
      <span class="brand-name">Altershilfe Plus</span>
    </div>
    <div class="rule" style="margin-top:0"></div>
    <div class="headline">
      <div class="kicker">Wir kümmern uns um</div>
      <div class="main">Ihre Bedürfnisse</div>
    </div>
    <div class="photo photo--hands" role="img" aria-label="Foto: gefaltete Hände eines älteren Menschen auf einem Gehstock"></div>
  </section>
</main>
</body>
</html>
```